Plastic Business Card for Bookkeeper

We are looking for a simple professional business card design to use for printing on thin frosted plastic (see-through) card stock. Logo and brand guideline documents are attached as well as a photo of our old business card, and another business card example that we like.

Target Market(s)

Small Business

Industry/Entity Type

Bookkeeper

Contact Information for Business Card

Harriet Valdez CPA
Chief Executive Bookkeeper
T. 03 5926 4187
M. 0432 861 507
E. harriet@quillpathledger.com
W. www.quillpathledger.com

Font styles to use
Sans Serif

Colors
6b449b
00a990

Requirements
Must have
• Stick with logo colors. Writing should be clear and easy to read and not too cramped together.
Nice to have
• Tag line for back of the card - 'Not your ordinary Bookkeeper'

```html
<!DOCTYPE html>
<html lang="en">
<head>
<meta charset="utf-8">
<title>Quillpath Ledger – Business Card</title>
<link rel="stylesheet" href="https://fonts.googleapis.com/css2?family=Montserrat:wght@400;600;700&family=Open+Sans:wght@400&family=EB+Garamond:ital@1&display=swap">
<style>
  :root {
    --purple: #6b449b;
    --purple-band: #6f4c9f;
    --teal: #00788f;
    --teal-mark: #0a7e8e;
    --frost-top: #f7f4f5;
    --frost-bottom: #ece6e8;
    --stage: #e4e1e3;
    --white: #ffffff;
  }
  * { box-sizing: border-box; margin: 0; padding: 0; }
  html, body { width: 1200px; height: 899px; overflow: hidden; }
  body { background: var(--stage); position: relative; font-family: "Open Sans", sans-serif; }

  .card {
    position: absolute;
    width: 563px; height: 348px;
    border-radius: 16px;
    overflow: hidden;
    background: linear-gradient(180deg, var(--frost-top), var(--frost-bottom));
    box-shadow: 0 6px 22px rgba(0,0,0,0.12);
  }
  .card--front { left: 205px; top: 92px; }
  .card--back  { left: 450px; top: 458px; }

  .band { position: absolute; left: 0; right: 0; top: 185px; bottom: 0; }
  .card--front .band { background: var(--purple-band); }
  .card--back .band  { background: var(--teal); }

  .brand { position: absolute; display: flex; align-items: center; gap: 20px; }
  .card--front .brand { left: 84px; top: 60px; }
  .brand-dot { width: 68px; height: 68px; border-radius: 50%; background: var(--teal-mark); flex: none; }
  .brand-name {
    font-family: "Montserrat", sans-serif; font-weight: 700;
    font-size: 25px; line-height: 34px; letter-spacing: 0.5px;
    color: var(--purple); text-transform: uppercase;
  }
  .card--back .brand { right: 83px; top: 60px; transform: scaleX(-1); opacity: 0.55; }

  .person { position: absolute; right: 305px; top: 240px; text-align: right; color: var(--white); }
  .person-name { font-family: "Montserrat", sans-serif; font-weight: 700; font-size: 20px; line-height: 24px; text-transform: uppercase; letter-spacing: -0.2px; }
  .person-role { font-size: 14.5px; line-height: 18px; }

  .divider { position: absolute; left: 280px; top: 233px; width: 1px; height: 81px; background: rgba(255,255,255,0.8); }

  .contact { position: absolute; left: 302px; top: 233px; list-style: none; color: var(--white); font-size: 15px; line-height: 20.5px; }
  .contact li { display: flex; align-items: center; gap: 5px; }
  .contact svg { width: 12px; height: 12px; fill: var(--white); flex: none; }

  .tagline {
    position: absolute; left: 0; right: 0; top: 210px;
    text-align: center; color: var(--white);
    font-family: "EB Garamond", serif; font-style: italic;
    font-size: 38px; line-height: 51px;
  }
</style>
</head>
<body>

<section class="card card--front" aria-label="Business card front">
  <div class="brand">
    <span class="brand-dot"></span>
    <p class="brand-name">Quillpath<br>Ledger</p>
  </div>
  <div class="band"></div>
  <div class="person">
    <p class="person-name">Harriet Valdez CPA</p>
    <p class="person-role">Chief Executive Bookkeeper</p>
  </div>
  <span class="divider"></span>
  <ul class="contact">
    <li><svg viewBox="0 0 12 12"><path d="M1 4c0-2 2-3 5-3s5 1 5 3l-2 1-1-2H4L3 5zM3 6h6l1 5H2z"/></svg>03 5926 4187</li>
    <li><svg viewBox="0 0 12 12"><path d="M3 0h6a1 1 0 0 1 1 1v10a1 1 0 0 1-1 1H3a1 1 0 0 1-1-1V1a1 1 0 0 1 1-1zm0 2v7h6V2z"/></svg>0432 861 507</li>
    <li><svg viewBox="0 0 12 12"><path d="M0 2h12v8H0zm1 1v.5l5 3.5 5-3.5V3z"/></svg>harriet@quillpathledger.com</li>
    <li><svg viewBox="0 0 12 12"><circle cx="6" cy="6" r="5.5"/></svg>www.quillpathledger.com</li>
  </ul>
</section>

<section class="card card--back" aria-label="Business card back">
  <div class="brand">
    <span class="brand-dot"></span>
    <p class="brand-name">Quillpath<br>Ledger</p>
  </div>
  <div class="band"></div>
  <p class="tagline">Not your ordinary<br>Bookkeeper</p>
</section>

</body>
</html>
```